Ebook/Booklet Cover: Neue Arbeitswelten
Tolles Miteinander, hat genau gefühlt und erkannt wo ich hin wollte. Und war sehr geduldig, da ich die letzten Informationen zum Buch jetzt erst mit großer Verspätung übermitteln konnte. Gerne jederzeit wieder!
Zielgruppe
Beratung und Training für kleine und mittlere Unternehmen im Bereich Arbeitnehmerschutz (Arbeitssicherheit), Stressprävention und Aufbau von alltagstauglichen Arbeitsabläufen/Strukturen.
In diesem Buchprojekt jetzt trete ich jedoch nicht primär als Unternehmen auf, sondern als Autorin.
Zielgruppe: Bis jetzt Führungskräfte, Geschäftsführer, Personalmanagement in Unternehmen.
Das soll auch so bleiben nur ist mein Plan in Zukunft auch Privatpersonen anzusprechen.
Inhalt des Ebooks:
Ratgeber, Impulsgeber und Informationsvermittler zu den Themen 'Hybrides Arbeiten', 'Arbeiten im Home Office', 'Digitales Arbeiten' .
Einzelne Themen sind jeweils in einem eigenen Ebook.
Titel ist noch in Arbeit. Es sollten jedoch 2 Zeilen sein.
Eines welches das Thema grob beschreibt - zB 'Perspektiven zur Arbeitswelt der Zukunft' (Das bleibt immer gleich) und darunter 'Hybrides Arbeiten' (Das ist bei jedem Thema dann extra)
Es geht inhaltlich darum, welche Folgen haben diese neuen Arbeitssituationen für Körper - Geist und Psyche und wie geht man im Idealfall damit um. Und wie bereiten wir uns für diese enormen Veränderungen in der ZUkunft optimal vor.
Mit dem Ziel, dass sich der Leser Tipps rauspickt die er selbst umsetzen kann zu Hause. Und vielleicht auch eine neue Perspektive in diese neue Arbeitswelt bekommt.
Und auch Unternehmer und Personalverantwortliche haben so einen Leitfaden für die Zukunft.
Man könnte sagen 'Hoch wissenschaftliche Inhalte + gesetzliche Vorgaben (Also teilweise komplizierte + trockene Inhalte) sollen niederschwellig, leicht lesbar und unterhaltsam präsentiert werden.
Aufgabenstellung
Ich mag Klares. Sauberes. Harmonisches. Ein Mix aus 'edel, niveauvoll, professionell' und 'sympathisch, fröhlich, stylisch'
Nichts Überladenes, keine Reizüberflutung.
Und es darf ein klein wenig darf 'Spiritualität' durchkommen - muss aber nicht.
Auf meiner Homepage sieht man eine Kugel zwischen 2 Händen. Diese passt zB sehr gut zu mir: Verbindend, harmonisch, klar, 'rund'.
Ich habe diese Velmora Bildarchiv Datei angefügt - muss aber nicht verwendet werden!
Weiter unten, wo der Regler zu verschieben ist um Vorstellungen einzugrenzen ist mir aufgefallen, dass dies gar nicht so einfach so beschreiben ist ;-). Wenn eine klare Struktur da ist (zB weißer Hintergrund), Farben harmonisch sind darf ein Teil gerne verspielt und bunt sein als Akzent. Aber eben nicht chaotisch überladen.
Vom Typ her bin ich eher 'HIN ZU statt WEG VON'. Ein Buchcover zum Thema 'Durch Entspannung weniger Stress' würde bei mir zB keinen Kopf zeigen der Blitze und Chaos um sich hat. Sondern ein Kopf der entspannte, bunte, fließende Gedanken hat.
Mei, ich hoffe Ihr Kreativen die das lest habt Eure Kristallkugel zum Gedankenlesen dabei,... ist gar nicht so einfach meine Vorstellung in Worte zu fassen :-).
Zur Preisgestaltung in dem Projekt: Ich bin (Wie viele von uns) finanziell recht gebeutelt durch die aktuelle Situation. Daher geht aktuell nur das Minibudget.
Ich plane hier aber Schritt für Schritt mehr zu machen (Als Autorin) in Zukunft und es ist absolut die Möglichkeit einer weiteren Zusammenarbeit vorhanden.
Liebe Grüße an Euch alle!!
Update:
zu viel schwarze Farbe ist nicht so meines ;-), - ich tendiere zu hellen Designs...

```html
<!DOCTYPE html>
<html lang="de">
<head>
<meta charset="utf-8">
<title>Hybrides Arbeiten – Buchumschlag</title>
<link href="https://fonts.googleapis.com/css2?family=Bebas+Neue&family=Oswald:wght@500&family=Catamaran:wght@400;500&family=Poppins:wght@400&family=Hind:ital,wght@0,400;1,400&display=swap" rel="stylesheet">
<style>
  :root {
    --mint: #b8dfdb;
    --orange: #e95d0f;
    --petrol: #3f6e80;
    --petrol-soft: #4d7587;
    --white: #ffffff;
  }
  html, body {
    margin: 0;
    padding: 0;
    width: 1200px;
    height: 833px;
    overflow: hidden;
    background: var(--mint);
  }
  .cover {
    position: relative;
    width: 1200px;
    height: 833px;
    background: var(--mint);
    overflow: hidden;
  }
  /* Back cover */
  .author-photo {
    position: absolute;
    left: 62px;
    top: 72px;
    width: 134px;
    height: 191px;
    background: linear-gradient(160deg, #cfd0d2 0%, #b9babd 55%, #e9e9ea 100%);
    z-index: 2;
  }
  .back-panel {
    position: absolute;
    left: 115px;
    top: 127px;
    width: 311px;
    height: 568px;
    background: var(--orange);
  }
  .back-text {
    position: absolute;
    left: 139px;
    top: 287px;
    width: 268px;
    color: var(--white);
    font-family: "Poppins", sans-serif;
    font-size: 11.6px;
    line-height: 15.6px;
    text-align: justify;
    hyphens: auto;
  }
  .back-text p {
    margin: 0 0 15.7px 0;
  }
  .call-to-action {
    position: absolute;
    left: 115px;
    width: 311px;
    top: 584px;
    text-align: center;
    color: var(--white);
    font-family: "Poppins", sans-serif;
    font-size: 15.6px;
    line-height: 21px;
  }
  .call-to-action p { margin: 0 0 6px 0; }
  /* Spine */
  .spine {
    position: absolute;
    left: 557px;
    top: 0;
    width: 62px;
    height: 833px;
    background: var(--orange);
  }
  .spine svg { position: absolute; left: 0; top: 0; }
  .spine-author {
    position: absolute;
    left: 0;
    width: 62px;
    top: 788px;
    text-align: center;
    color: var(--white);
    font-family: "Catamaran", sans-serif;
    font-size: 11.5px;
    line-height: 14.5px;
  }
  /* Front cover */
  .front-title { position: absolute; left: 0; top: 0; }
  .title-main { font-family: "Bebas Neue", sans-serif; fill: var(--orange); }
  .title-sub { font-family: "Catamaran", sans-serif; font-weight: 500; fill: var(--petrol); letter-spacing: 1px; }
  .front-illustration {
    position: absolute;
    left: 636px;
    top: 378px;
    width: 541px;
    height: 377px;
    background:
      radial-gradient(ellipse at 35% 55%, #8e6fa3 0%, rgba(142,111,163,0) 40%),
      radial-gradient(ellipse at 72% 45%, #e3a77f 0%, rgba(227,167,127,0) 35%),
      linear-gradient(135deg, #d8763d 0%, #b8dfdb 60%, #b8dfdb 100%);
    opacity: 0.85;
  }
  .front-tagline {
    position: absolute;
    left: 677px;
    top: 775px;
    width: 486px;
    color: var(--petrol-soft);
    font-family: "Hind", sans-serif;
    font-style: italic;
    font-size: 17px;
    line-height: 20.5px;
    letter-spacing: 0.6px;
    text-align: justify;
    text-align-last: justify;
  }
</style>
</head>
<body>
<main class="cover">

  <section class="back-cover">
    <div class="back-panel"></div>
    <div class="author-photo" role="img" aria-label="Porträtfoto der Autorin vor hellgrauem Hintergrund"></div>
    <div class="back-text">
      <p>Dank „Wissen klar erklärt“ werden Sie beim Lesen von Nachrichten nicht mehr von Überlegungen abgelenkt, was diese oder jene Begriffe zu bedeuten haben.</p>
      <p>Sie bilden außerdem faktenbasiert eine eigene, gut begründete Meinung und können politische Diskussionen auf Augenhöhe verfolgen und sogar souverän führen.</p>
      <p>Sie erkennen die Probleme der aktuellen Politik und können somit frühzeitig erkennen was für berufliche wie private Folgen auf Ihr Leben haben könnte.</p>
      <p>Mit Ihrem Wissen können Sie andere Menschen aufklären und für die Zusammenhänge der aktuellen Lage begeistern.</p>
    </div>
    <div class="call-to-action">
      <p>WORAUF WARTEN SIE NOCH?</p>
      <p>GESTALTEN SIE JETZT<br>UNSERE ZUKUNFT MIT!</p>
    </div>
  </section>

  <section class="spine">
    <svg width="62" height="833" viewBox="0 0 62 833">
      <text class="title-main" font-size="50" fill="#ffffff" transform="translate(608 754) rotate(-90)" textLength="279" lengthAdjust="spacingAndGlyphs" style="fill:#ffffff">HYBRIDES ARBEITEN</text>
      <text font-family="Oswald, sans-serif" font-weight="500" font-size="30" fill="#ffffff" transform="translate(601 412) rotate(-90)" textLength="232" lengthAdjust="spacingAndGlyphs">Arbeiten im Home Office</text>
    </svg>
    <div class="spine-author">Hanne<br>Winter</div>
  </section>

  <section class="front-cover">
    <svg class="front-title" width="1200" height="380" viewBox="0 0 1200 380">
      <text class="title-main" x="727" y="136" font-size="146" textLength="395" lengthAdjust="spacingAndGlyphs">HYBRIDES</text>
      <text class="title-sub" x="1124" y="168" font-size="27" text-anchor="end">Digitales Arbeiten</text>
      <text class="title-main" x="729" y="296" font-size="143" textLength="392" lengthAdjust="spacingAndGlyphs">ARBEITEN</text>
      <text class="title-sub" x="1126" y="329" font-size="28" text-anchor="end">Arbeiten im Home Office</text>
      <text class="title-sub" x="1146" y="361" font-size="17.5" text-anchor="end" style="letter-spacing:0.5px">Hanne Winter</text>
    </svg>
    <div class="front-illustration" role="img" aria-label="Illustration: Frau am Schreibtisch blickt skeptisch auf einen Vorgesetzten, der aus dem Bildschirm ragt; dahinter Uhr und Pflanze"></div>
    <p class="front-tagline">Ein Ratgeber, Impulsgeber und Informationsvermittler für Führungskräfte, Geschäftsführer und Personalmanagement</p>
  </section>

</main>
</body>
</html>
```